Medical consulting firm needs polished website

I am a physician and working on setting up a smal consulting firm in New Hampshire, USA. It is called Brightwell Health Guidance, LLC and the website will be BrightwellCare.com. I was puttering around at making my own website, and it just didn't come together nicely so I've decided to leave it to the pros. The focus of the business is Advanced Care Planning, ie planning for your future medical needs. So it deals with some heavy stuff like planning for if you get sick, who should make decisions for you, end of life options etc. So it can't be too flippant or cutesy, but also can't be too dour and dark. I am hoping to convey that by thinking ahead and making some plans you can lift some of the worries off of yourself and your family - and that we can help make a scary sounding path more manageable. I want it to be made with wordpress and I have actually already bought a template ( Curavia – A Fresh Comprehensive Clinical & Wellness Theme ). The website needs to have general information about our services, doc profile, appointment maker, blog/url link page, and ideally web commerce application ( the template has access to woocommerce). I've posted my business card and current brochure (still tweaking them, but you get the idea). I am also partnering with lifemapper.com and so have included their logo and would want connections/info about them. I have the logos etc in different formats as needed.

middle aged to older adults

Medical

Coded - Design and coding required

Sans Serif

• as above.
• Ease of reading/access for elderly viewers. woo commerce.

```html
<!DOCTYPE html>
<html lang="en">
<head>
<meta charset="utf-8">
<title>Brightwell Health Guidance</title>
<link href="https://fonts.googleapis.com/css2?family=Open+Sans:ital,wght@0,300;0,400;0,600;0,700;0,800;1,400&display=swap" rel="stylesheet">
<style>
:root{
  --blue:#2f8fcf;
  --blue-dark:#2478b3;
  --ink:#333;
  --text:#666;
  --muted:#999;
  --rule:#e3e3e3;
  --band:#f7f7f7;
  --white:#fff;
  --dash:#444;
}
*{margin:0;padding:0;box-sizing:border-box}
html,body{width:1200px;height:1200px;overflow:hidden;background:var(--white)}
body{font-family:"Open Sans",Arial,sans-serif;color:var(--text)}
.canvas{position:relative;width:1200px;height:1200px;overflow:hidden}
.abs{position:absolute}
.services-band{left:0;top:0;width:1200px;height:588px;background:var(--band)}
.top-tab{left:556px;top:0;width:63px;height:3px;background:var(--blue)}
.section-title{position:absolute;font-size:22px;font-weight:300;color:var(--blue);letter-spacing:.2px;line-height:1}
.section-title b{font-weight:700}
.title-rule{position:absolute;height:3px;border-top:1px solid var(--rule);border-bottom:1px solid var(--rule)}
.pager-dash{position:absolute;top:55px;width:20px;height:3px;background:var(--dash)}
.photo{position:absolute}
.service{position:absolute;top:402px;width:280px}
.service h3{font-size:13.6px;font-weight:600;color:var(--blue);line-height:18px}
.service .role{font-size:8px;color:var(--muted);text-transform:uppercase;line-height:12px}
.service p{margin-top:10px;font-size:10.4px;line-height:14.4px;color:var(--text)}
.service .link{display:block;margin-top:18px;font-size:10.4px;font-style:italic;color:var(--blue)}
.news-card{position:absolute;background:var(--white);border:1px solid #e4e4e4}
.news-card .img{position:relative;border-bottom:3px solid var(--blue)}
.date{position:absolute;left:0;top:0;width:59px;height:59px;background:var(--blue);color:var(--white);padding:6px 0 0 10px}
.date .day{font-size:30px;font-weight:800;line-height:30px;letter-spacing:-1px}
.date .mon{font-size:9.5px;line-height:14px}
.news-body{padding:8px 12px 0 12px}
.news-body h4{font-size:16px;font-weight:400;color:var(--ink);line-height:21px}
.meta{margin-top:6px;font-size:8.6px;color:var(--text)}
.meta span{color:#bbb;margin:0 3px}
.news-body p{margin-top:7px;font-size:10.4px;line-height:14.4px}
.btn{display:inline-block;margin-top:8px;background:var(--blue);color:var(--white);font-size:9.8px;padding:0 19px;height:32px;line-height:30px;border-bottom:3px solid var(--blue-dark);border-radius:2px}
.doctor{position:absolute;left:802px;top:690px;width:288px;text-align:center}
.avatar{margin:0 auto;width:140px;height:140px;border-radius:50%;border:4px solid var(--white);box-shadow:0 0 0 1px #ddd}
.doctor h3{margin-top:12px;font-size:15px;font-weight:600;color:var(--ink);line-height:18px}
.doctor .role{font-size:9.5px;color:var(--ink);line-height:12px}
.doctor p{margin:10px auto 0;width:252px;font-size:10.4px;line-height:14.4px;color:var(--muted)}
.dots{position:absolute;top:947px;height:3px}
.acc{position:absolute;left:802px;width:288px}
.acc-head{display:flex;align-items:center;gap:9px;font-size:13px;line-height:18px}
.acc-box{width:17px;height:17px;display:flex;align-items:center;justify-content:center}
.acc p{margin:12px 0 0 12px;width:258px;font-size:10.4px;line-height:14.4px;color:var(--text)}
</style>
</head>
<body>
<div class="canvas">
  <div class="abs services-band"></div>
  <div class="abs top-tab"></div>

  <h2 class="section-title" style="left:189px;top:47px">OUR <b>SERVICES</b></h2>
  <div class="pager-dash" style="left:1036px"></div>
  <div class="pager-dash" style="left:1058px"></div>
  <div class="title-rule" style="left:189px;top:75px;width:889px"></div>

  <div class="photo" role="img" aria-label="Physician reviewing planning documents with an older patient" style="left:190px;top:99px;width:280px;height:280px;background:linear-gradient(135deg,#dfe6ee,#f4f6f8 55%,#c9d3de)"></div>
  <div class="photo" role="img" aria-label="Adult children and parent talking together at a kitchen table" style="left:494px;top:99px;width:280px;height:280px;background:linear-gradient(160deg,#e9edf2,#cfdcea 50%,#7ea3d6)"></div>
  <div class="photo" role="img" aria-label="Calm garden path in soft morning light" style="left:798px;top:99px;width:280px;height:280px;background:linear-gradient(135deg,#f3f5f7,#e6ebf0 55%,#d2dbe4)"></div>

  <div class="service" style="left:189px">
    <h3>ADVANCE DIRECTIVES</h3>
    <div class="role">One-on-one physician consult</div>
    <p>Put your wishes for future medical care in writing, in plain language. We walk through each choice with you, answer your questions and help you complete the forms, so your doctors and family know what matters most to you.</p>
    <span class="link">- Learn More</span>
  </div>
  <div class="service" style="left:493px">
    <h3>HEALTH CARE PROXY</h3>
    <div class="role">Family planning meeting</div>
    <p>Choose the person who will speak for you if you cannot speak for yourself. We help you pick the right person, prepare them for the role and guide a gentle family talk, so no one is left guessing in a hard moment.</p>
    <span class="link">- Learn More</span>
  </div>
  <div class="service" style="left:797px">
    <h3>END-OF-LIFE OPTIONS</h3>
    <div class="role">Guidance and resources</div>
    <p>Understand the options for comfort, hospice and care at home, explained clearly and without pressure. Thinking ahead lifts worry from you and your loved ones and makes the path ahead feel far more manageable.</p>
    <span class="link">- Learn More</span>
  </div>

  <h2 class="section-title" style="left:178px;top:629px">LATEST <b>NEWS</b></h2>
  <div class="title-rule" style="left:178px;top:658px;width:600px"></div>
  <h2 class="section-title" style="left:802px;top:629px">MEET THE <b>DOCTOR</b></h2>
  <div class="title-rule" style="left:802px;top:658px;width:288px"></div>

  <article class="news-card" style="left:178px;top:690px;width:236px;height:355px">
    <div class="img" role="img" aria-label="Older couple reading together on a sofa" style="height:175px;background:linear-gradient(135deg,#e8edf1,#f5f7f8 50%,#2ea0d8 100%)">
      <div class="date"><div class="day">29</div><div class="mon">FEB 2014</div></div>
    </div>
    <div class="news-body">
      <h4>Starting the Conversation With Family</h4>
      <div class="meta">By: Dr. Halvik<span>|</span>Tags: Family, Planning, Proxy</div>
      <p>Simple ways to begin talking about your care wishes, and why it helps everyone feel calmer...</p>
      <span class="btn">READ MORE</span>
    </div>
  </article>

  <article class="news-card" style="left:438px;top:690px;width:340px;height:350px">
    <div class="img" role="img" aria-label="Physician and patient talking in a bright office" style="height:205px;background:linear-gradient(135deg,#c9d6e2,#e4ebf1 45%,#8ec8d8 100%)">
      <div class="date"><div class="day">29</div><div class="mon">FEB 2014</div></div>
    </div>
    <div class="news-body">
      <h4 style="margin-top:2px">What an Advance Directive Covers</h4>
      <div class="meta">By: Dr. Halvik<span>|</span>Tags: Directives, Forms, Planning</div>
      <p>A clear guide to the choices in a directive, from treatment wishes to naming a proxy...</p>
      <span class="btn">READ MORE</span>
    </div>
  </article>

  <article class="news-card" style="left:178px;top:1078px;width:236px;height:140px;border:none">
    <div role="img" aria-label="Hands holding a cup of tea beside paperwork" style="height:140px;background:linear-gradient(135deg,#5fb6d8,#9fd4e6 50%,#2f86b6)">
      <div class="date"><div class="day">29</div><div class="mon">FEB 2014</div></div>
    </div>
  </article>
  <article class="news-card" style="left:438px;top:1072px;width:340px;height:140px;border:none">
    <div role="img" aria-label="Older adult walking outdoors on a sunny trail" style="height:140px;background:linear-gradient(135deg,#f0e4dc,#dbe8f2 50%,#8fa3b5)">
      <div class="date"><div class="day">29</div><div class="mon">FEB 2014</div></div>
    </div>
  </article>

  <div class="doctor">
    <div class="avatar" role="img" aria-label="Portrait of the founding physician" style="background:radial-gradient(circle at 50% 40%,#eef3f5,#bfe3df 60%,#5fc7c0)"></div>
    <h3>NORA HALVIK, MD</h3>
    <div class="role">FOUNDER &amp; PHYSICIAN</div>
    <p>Board-certified physician helping New Hampshire families plan future care with clarity, kindness and plain answers.</p>
  </div>
  <div class="dots" style="left:912px;width:19px;background:var(--blue)"></div>
  <div class="dots" style="left:936px;width:19px;background:var(--dash)"></div>
  <div class="dots" style="left:958px;width:19px;background:var(--dash)"></div>

  <h2 class="section-title" style="left:802px;top:990px">BRIGHTWELL <b>GUIDE</b></h2>
  <div class="title-rule" style="left:802px;top:1019px;width:288px"></div>

  <div class="acc" style="top:1050px">
    <div class="acc-head" style="color:var(--blue)">
      <span class="acc-box" style="background:var(--blue)"><svg width="8" height="8" viewBox="0 0 8 8"><rect x="0" y="3" width="8" height="2" fill="#fff"/></svg></span>
      Advance Directive Review
    </div>
    <p>Bring your existing forms or start fresh. We review what you have, explain each section in everyday words, note anything missing and make sure the final copy is signed, witnessed and shared with the people who need it.</p>
  </div>
  <div class="abs" style="left:802px;top:1174px;width:288px;height:1px;background:var(--rule)"></div>
  <div class="acc" style="top:1184px">
    <div class="acc-head" style="color:var(--ink)">
      <span class="acc-box" style="background:var(--dash)"><svg width="8" height="8" viewBox="0 0 8 8"><rect x="0" y="3" width="8" height="2" fill="#fff"/><rect x="3" y="0" width="2" height="8" fill="#fff"/></svg></span>
      Choosing a Health Care Proxy
    </div>
  </div>
</div>
</body>
</html>
```